Business Card

Just need business logo with phone number on it. 0487 312 556
And the following on the bottom of the card.

"Your local plumbing experts".
and emblems for kelpa card, cheque and cash

```html
<!DOCTYPE html>
<html lang="en">
<head>
<meta charset="utf-8">
<title>Ridgeline Plumbing &amp; Drainage – Business Card</title>
<link rel="stylesheet" href="https://fonts.googleapis.com/css2?family=Roboto:wght@400;500;900&display=swap">
<style>
  :root {
    --page-bg: #eceae6;
    --card-white: #ffffff;
    --brand-blue: #1fa9d6;
    --brand-blue-deep: #1795c4;
    --brand-red: #e0243a;
    --cash-green: #3f6a4a;
    --cheque-slate: #5d6f86;
  }
  * { box-sizing: border-box; margin: 0; padding: 0; }
  html, body {
    width: 1200px;
    height: 780px;
    overflow: hidden;
    background: var(--page-bg);
    font-family: "Roboto", Arial, sans-serif;
  }
  .card {
    position: absolute;
    left: 100px;
    top: 100px;
    width: 1000px;
    height: 580px;
    background: var(--card-white);
    overflow: hidden;
    box-shadow: 0 10px 30px rgba(0, 0, 0, 0.18);
  }
  .card-backdrop {
    position: absolute;
    inset: 0;
    width: 100%;
    height: 100%;
  }
  .card-content {
    position: absolute;
    left: 70px;
    top: 80px;
    width: 620px;
  }
  .brand {
    display: flex;
    align-items: center;
    gap: 22px;
    color: var(--brand-red);
    font-weight: 900;
    text-transform: uppercase;
  }
  .brand-dot {
    width: 70px;
    height: 70px;
    border-radius: 50%;
    background: var(--brand-blue);
    flex: none;
  }
  .brand-name {
    line-height: 1;
  }
  .brand-initials { display: block; font-size: 76px; letter-spacing: -1px; }
  .brand-main { display: block; font-size: 46px; margin-top: 4px; }
  .brand-sub { display: block; font-size: 22px; letter-spacing: 6px; margin-top: 6px; }
  .brand-suffix { display: block; font-size: 12px; letter-spacing: 3px; margin-top: 6px; }
  .phone {
    margin: 42px 0 0 92px;
    color: var(--brand-blue);
    font-size: 44px;
    font-weight: 500;
    letter-spacing: 1px;
  }
  .payment-methods {
    display: flex;
    align-items: center;
    gap: 40px;
    margin: 42px 0 0 92px;
  }
  .payment-card {
    color: var(--brand-blue-deep);
    font-size: 30px;
    font-weight: 900;
  }
  .payment-cash {
    width: 62px;
    height: 62px;
    border-radius: 50%;
    background: var(--cash-green);
  }
  .payment-cheque {
    width: 78px;
    height: 56px;
    border-radius: 6px;
    background: var(--cheque-slate);
  }
  .tagline {
    position: absolute;
    left: 162px;
    bottom: 40px;
    color: var(--brand-blue);
    font-size: 30px;
    font-weight: 400;
    letter-spacing: 1px;
  }
</style>
</head>
<body>
  <div class="card">
    <svg class="card-backdrop" viewBox="0 0 1000 580" preserveAspectRatio="none" aria-hidden="true">
      <rect width="1000" height="580" fill="var(--brand-blue)"/>
      <circle cx="420" cy="300" r="575" fill="var(--brand-red)"/>
      <circle cx="370" cy="300" r="570" fill="var(--card-white)"/>
    </svg>

    <div class="card-content">
      <div class="brand">
        <span class="brand-dot"></span>
        <span class="brand-name">
          <span class="brand-initials">RPD</span>
          <span class="brand-main">Ridgeline</span>
          <span class="brand-sub">Plumbing &amp; Drainage</span>
          <span class="brand-suffix">Pty Ltd</span>
        </span>
      </div>

      <p class="phone">0487 312 556</p>

      <div class="payment-methods">
        <span class="payment-card">kelpa</span>
        <span class="payment-cash" role="img" aria-label="Cash payment emblem"></span>
        <span class="payment-cheque" role="img" aria-label="Cheque payment emblem"></span>
      </div>
    </div>

    <p class="tagline">Your local plumbing experts</p>
  </div>
</body>
</html>
```